Real Estate Webpage Design

We have an existing website: brindlewoodhomes.com.au
We focus customised service mainly on Property Management and second-hand property sales.
We are not entirely happy about the current design and layout can stay roughly the same as the back end coding is linked to a CRM system.
We would like to see the design are more reachable to our clients and appearing.
Please check our Website Design Draft for more details.

Industry/Entity Type

Real estate Agency

Number of Pages Required

5+ page

Font styles to use
Sans Serif

Colors

Designer to choose colors to be used in the design.

```html
<!DOCTYPE html>
<html lang="en">
<head>
<meta charset="utf-8">
<title>Brindlewood Homes – Real Estate</title>
<link href="https://fonts.googleapis.com/css2?family=Poppins:wght@400;500;600;700&display=swap" rel="stylesheet">
<style>
:root{
  --yellow:#f9b41b;
  --navy:#1c2f45;
  --ink:#1f2a36;
  --grey:#6c7480;
  --light:#f3f3f3;
  --white:#ffffff;
}
*{box-sizing:border-box;margin:0;padding:0}
html,body{width:1200px;height:3596px;overflow:hidden}
body{font-family:'Poppins',sans-serif;color:var(--ink);background:var(--white);font-size:12px;line-height:1.6}
section,header,footer{position:relative;width:1200px}
.btn{display:inline-block;border-radius:20px;padding:8px 22px;font-size:11px;font-weight:500;text-decoration:none}
.btn-yellow{background:var(--yellow);color:var(--white)}
.btn-navy{background:var(--navy);color:var(--white)}
.abs{position:absolute}
.brand{font-weight:700;color:var(--yellow);font-size:22px;display:flex;align-items:center;gap:8px;line-height:1}
.brand-dot{width:16px;height:16px;background:var(--yellow)}

/* header */
.site-header{height:72px;display:flex;align-items:center;justify-content:space-between;padding:0 60px 0 100px;background:var(--white)}
.main-nav{display:flex;gap:6px}
.main-nav a{font-size:11px;color:var(--ink);text-decoration:none;padding:6px 16px;border-radius:16px}
.main-nav a.active{background:var(--yellow);color:var(--white)}

/* hero */
.hero{height:480px;background:linear-gradient(180deg,#8fa6bd 0%,#b9c4cc 45%,#6f7479 100%)}
.hero-photo{position:absolute;inset:0;background:linear-gradient(180deg,rgba(20,35,55,.35),rgba(20,35,55,.55))}
.hero h1{position:absolute;top:190px;width:100%;text-align:center;color:var(--white);font-size:40px;font-weight:600}
.hero .tagline{position:absolute;top:252px;left:50%;transform:translateX(-50%);background:rgba(40,90,140,.75);color:var(--white);font-size:16px;padding:2px 14px}
.hero .btn{position:absolute;top:300px;left:50%;transform:translateX(-50%)}

/* about */
.about{height:488px}
.about-title{left:100px;top:100px;font-size:40px;font-weight:700;color:var(--navy);line-height:1.15}
.about-title .small{display:inline-block;font-size:12px;font-weight:500;background:var(--white);color:var(--navy);border-bottom:3px solid var(--yellow);padding:0 8px;margin-left:-4px;vertical-align:middle}
.about-text{left:100px;top:228px;width:440px;color:var(--grey);font-size:11px}
.about-text p{margin-bottom:14px}
.about-actions{left:100px;top:376px;display:flex;gap:14px}
.about-block{left:940px;top:40px;width:260px;height:400px;background:var(--yellow)}
.about-photo{left:620px;top:68px;width:430px;height:360px;background:linear-gradient(160deg,#c9d4de,#9c7a5c 70%,#6d7a55)}

/* services */
.services{height:720px;background:var(--light)}
.svc{position:absolute}
.svc-photo-a{left:100px;top:76px;width:600px;height:284px;background:linear-gradient(170deg,#7ea3c6,#b06a3c 55%,#6a5a3a)}
.svc-panel{background:var(--navy);color:var(--white);padding:34px 36px}
.svc-panel h2{font-size:20px;font-weight:500;margin-bottom:12px;padding-bottom:6px;border-bottom:2px solid var(--yellow);display:inline-block}
.svc-panel p{font-size:11px;color:#c9d2dc;margin-bottom:18px}
.svc-mgmt{left:700px;top:76px;width:400px;height:284px}
.svc-sales{left:100px;top:360px;width:400px;height:336px}
.svc-photo-b{left:500px;top:360px;width:400px;height:336px;background:linear-gradient(170deg,#a8c4db,#8a5a34 60%,#5c4a33)}
.svc-photo-c{left:916px;top:360px;width:184px;height:336px;background:linear-gradient(170deg,#8fb0cc,#7a6048 60%,#4d5a3b)}

/* listings */
.listings{height:680px}
.section-title{font-size:24px;font-weight:600;color:var(--navy);line-height:1.2;position:absolute}
.corner{position:absolute;left:-14px;top:-8px;width:12px;height:12px;border-left:3px solid var(--yellow);border-top:3px solid var(--yellow)}
.tabs{right:100px;top:104px;display:flex;gap:10px}
.tabs span{font-size:11px;padding:6px 18px;border-radius:16px;border:1px solid #dcdcdc;background:var(--white)}
.tabs span.active{background:var(--yellow);color:var(--white);border-color:var(--yellow)}
.cards{left:100px;top:196px;display:flex;gap:20px}
.card{width:235px;height:376px;background:var(--white);box-shadow:0 2px 12px rgba(0,0,0,.1);border-radius:4px;overflow:hidden}
.card-photo{height:160px}
.card-body{padding:12px 14px;font-size:10px}
.card-status{color:var(--grey);font-size:9px}
.card-addr{font-weight:600;font-size:11px;color:var(--navy);margin:2px 0 8px}
.card-feat{display:flex;gap:12px;align-items:center;margin-bottom:8px;color:var(--ink)}
.card-feat svg{width:12px;height:12px;margin-right:3px;vertical-align:-2px}
.price{font-weight:600;font-size:11px}
.open{color:var(--grey);font-size:9px;margin-top:4px}
.card-icons{display:flex;gap:10px;margin-top:18px}
.view-more{left:540px;top:628px}

/* contact */
.contact{height:420px;background:var(--yellow);color:var(--white)}
.contact h2{position:absolute;top:60px;width:100%;text-align:center;font-size:28px;font-weight:600}
.contact .lead{position:absolute;top:106px;left:380px;width:440px;text-align:center;font-size:11px}
.form{position:absolute;left:340px;top:164px;width:520px}
.form-row{display:flex;gap:40px;margin-bottom:18px}
.field{flex:1;border-bottom:1px solid var(--white);font-size:11px;padding-bottom:4px}
.field.tall{height:54px}
.form .btn{display:block;width:100px;margin:24px auto 0;text-align:center}

/* testimonials */
.testimonials{height:260px}
.quote-mark{left:586px;top:100px;font-size:48px;font-weight:700;color:var(--navy);line-height:1}
.stars{left:540px;top:150px;display:flex;gap:6px}
.testimonial-text{left:340px;top:182px;width:520px;text-align:center;font-size:11px;color:var(--grey)}
.author{left:0;top:236px;width:1200px;text-align:center;font-size:11px;font-weight:500}
.arrow{top:160px}

/* footer */
.site-footer{height:400px;background:var(--light)}
.foot-about{left:100px;top:40px;width:250px;font-size:10px;color:var(--grey)}
.foot-about .brand{margin-bottom:18px}
.foot-col{top:40px;font-size:10px;color:var(--grey)}
.foot-col h3{font-size:11px;font-weight:600;color:var(--navy);margin-bottom:10px}
.foot-col li{list-style:none;margin-bottom:2px}
.foot-col .line{display:flex;gap:8px;margin-bottom:10px;align-items:flex-start}
.socials{display:flex;gap:8px}
.socials span{width:22px;height:22px;border-radius:50%;background:var(--white);border:1px solid #ddd}
.bottom-bar{position:absolute;left:0;top:3520px;width:1200px;height:76px;border-top:1px solid #e2e2e2;display:flex;justify-content:space-between;align-items:center;padding:0 100px;font-size:9px;color:var(--grey);background:var(--white)}
</style>
</head>
<body>

<header class="site-header">
  <div class="brand"><span class="brand-dot"></span>Brindlewood Homes</div>
  <nav class="main-nav">
    <a class="active" href="#">Home</a><a href="#">About Us</a><a href="#">Leasing</a><a href="#">Buy</a><a href="#">Sell</a><a href="#">Our Team</a><a href="#">Blog</a><a href="#">Contact Us</a>
  </nav>
</header>

<section class="hero">
  <div class="hero-photo" role="img" aria-label="Modern two-storey townhouse with timber fence under a blue sky"></div>
  <h1>Find your dream home with Brindlewood</h1>
  <div class="tagline">Your trust real estate property partner</div>
  <a class="btn btn-yellow" href="#">Request a free appraisal</a>
</section>

<section class="about">
  <div class="abs about-block"></div>
  <div class="abs about-photo" role="img" aria-label="Brick cottage with front garden and tree"></div>
  <h2 class="abs about-title">Brindlewood<br><span class="small">A name for</span> “the home”</h2>
  <div class="abs about-text">
    <p>At Brindlewood Homes, the home is where everything starts. We are a local agency that treats every property as a place people live, not just an address on a list.</p>
    <p>Being committed to tailored service, our team looks after landlords, tenants, buyers and sellers with care. We combine honest advice, clear communication and local market knowledge so you always know where you stand.</p>
  </div>
  <div class="abs about-actions">
    <a class="btn btn-navy" href="#">Learn more</a>
    <a class="btn btn-yellow" href="#">Contact us</a>
  </div>
</section>

<section class="services">
  <div class="svc svc-photo-a" role="img" aria-label="Single-storey brick home with lawn at dusk"></div>
  <div class="svc svc-panel svc-mgmt">
    <h2>Property Management</h2>
    <p>We look after your investment as if it were our own. From finding quality tenants and routine inspections to rent collection and maintenance, our managers keep your property performing and your tenants happy, all year round.</p>
    <a class="btn btn-yellow" href="#">Request a free appraisal</a>
  </div>
  <div class="svc svc-panel svc-sales">
    <h2>Property Sales</h2>
    <p>Selling a second-hand home needs a clear plan. We prepare a tailored campaign, present your property at its best and negotiate hard for the right price, keeping you informed at every step of the sale.</p>
    <a class="btn btn-yellow" href="#">Request a free appraisal</a>
  </div>
  <div class="svc svc-photo-b" role="img" aria-label="Two-storey brick house with timber balcony"></div>
  <div class="svc svc-photo-c" role="img" aria-label="Timber pergola over a garden courtyard"></div>
</section>

<section class="listings">
  <h2 class="section-title" style="left:100px;top:96px"><span class="corner"></span>This month at Brindlewood<br>Homes</h2>
  <div class="abs tabs"><span>For Sale</span><span class="active">For Lease</span><span>Open Times</span><span>Sold</span><span>Leased</span></div>
  <div class="abs cards">
    <article class="card">
      <div class="card-photo" role="img" aria-label="Empty bright living room" style="background:linear-gradient(160deg,#e7e7e4,#bdb7ad)"></div>
      <div class="card-body">
        <div class="card-status">Leased</div>
        <div class="card-addr">2/14 Alder Grove, Ferncliff</div>
        <div class="card-feat"><span><svg viewBox="0 0 12 12"><rect x="1" y="5" width="10" height="5" fill="#1c2f45"/></svg>2</span><span><svg viewBox="0 0 12 12"><circle cx="6" cy="6" r="4" fill="#1c2f45"/></svg>1</span><span><svg viewBox="0 0 12 12"><rect x="2" y="3" width="8" height="6" rx="2" fill="#1c2f45"/></svg>1</span></div>
        <div class="price">$420 pw</div>
        <div class="open">Open: Sat 10:00 – 10:15 am</div>
        <div class="card-icons"><svg width="12" height="12"><rect width="12" height="12" fill="none" stroke="#6c7480"/></svg><svg width="12" height="12" viewBox="0 0 12 12"><polygon points="6,0 7.8,4 12,4.5 8.8,7.4 9.7,12 6,9.7 2.3,12 3.2,7.4 0,4.5 4.2,4" fill="#f9b41b"/></svg></div>
      </div>
    </article>
    <article class="card">
      <div class="card-photo" role="img" aria-label="Two-storey house with garage" style="background:linear-gradient(170deg,#9fbbd4,#6f6a66)"></div>
      <div class="card-body">
        <div class="card-status">For Lease</div>
        <div class="card-addr">9 Wattle Street, Ridgeview</div>
        <div class="card-feat"><span><svg viewBox="0 0 12 12"><rect x="1" y="5" width="10" height="5" fill="#1c2f45"/></svg>4</span><span><svg viewBox="0 0 12 12"><circle cx="6" cy="6" r="4" fill="#1c2f45"/></svg>2</span><span><svg viewBox="0 0 12 12"><rect x="2" y="3" width="8" height="6" rx="2" fill="#1c2f45"/></svg>2</span></div>
        <div class="price">$690 pw</div>
        <div class="open">Open: Sat 11:00 – 11:15 am</div>
        <div class="card-icons"><svg width="12" height="12"><rect width="12" height="12" fill="none" stroke="#6c7480"/></svg><svg width="12" height="12" viewBox="0 0 12 12"><polygon points="6,0 7.8,4 12,4.5 8.8,7.4 9.7,12 6,9.7 2.3,12 3.2,7.4 0,4.5 4.2,4" fill="#f9b41b"/></svg></div>
      </div>
    </article>
    <article class="card">
      <div class="card-photo" role="img" aria-label="Furnished lounge room" style="background:linear-gradient(160deg,#d9cfc2,#5e5048)"></div>
      <div class="card-body">
        <div class="card-status">For Lease</div>
        <div class="card-addr">3/5 Banksia Court, Elmsdale</div>
        <div class="card-feat"><span><svg viewBox="0 0 12 12"><rect x="1" y="5" width="10" height="5" fill="#1c2f45"/></svg>3</span><span><svg viewBox="0 0 12 12"><circle cx="6" cy="6" r="4" fill="#1c2f45"/></svg>1</span><span><svg viewBox="0 0 12 12"><rect x="2" y="3" width="8" height="6" rx="2" fill="#1c2f45"/></svg>1</span></div>
        <div class="price">$510 pw</div>
        <div class="open">Open: Sun 9:30 – 9:45 am</div>
        <div class="card-icons"><svg width="12" height="12"><rect width="12" height="12" fill="none" stroke="#6c7480"/></svg><svg width="12" height="12" viewBox="0 0 12 12"><polygon points="6,0 7.8,4 12,4.5 8.8,7.4 9.7,12 6,9.7 2.3,12 3.2,7.4 0,4.5 4.2,4" fill="#f9b41b"/></svg></div>
      </div>
    </article>
    <article class="card">
      <div class="card-photo" role="img" aria-label="Brick house with front lawn" style="background:linear-gradient(170deg,#8fb2d6,#9a5e44 60%,#6f7d4f)"></div>
      <div class="card-body">
        <div class="card-status">Leased</div>
        <div class="card-addr">1 Linden Road, Ferncliff</div>
        <div class="card-feat"><span><svg viewBox="0 0 12 12"><rect x="1" y="5" width="10" height="5" fill="#1c2f45"/></svg>3</span><span><svg viewBox="0 0 12 12"><circle cx="6" cy="6" r="4" fill="#1c2f45"/></svg>2</span><span><svg viewBox="0 0 12 12"><rect x="2" y="3" width="8" height="6" rx="2" fill="#1c2f45"/></svg>2</span></div>
        <div class="price">$560 pw</div>
        <div class="open">Open: Sat 1:00 – 1:15 pm</div>
        <div class="card-icons"><svg width="12" height="12"><rect width="12" height="12" fill="none" stroke="#6c7480"/></svg><svg width="12" height="12" viewBox="0 0 12 12"><polygon points="6,0 7.8,4 12,4.5 8.8,7.4 9.7,12 6,9.7 2.3,12 3.2,7.4 0,4.5 4.2,4" fill="#f9b41b"/></svg></div>
      </div>
    </article>
  </div>
  <a class="abs btn btn-navy view-more" href="#">View more</a>
</section>

<section class="contact">
  <h2>Get in touch</h2>
  <p class="lead">Whether you are leasing, buying or selling, our friendly team is ready to help. Send us a message and we will reply shortly.</p>
  <form class="form">
    <div class="form-row"><div class="field">Name</div><div class="field">Surname</div></div>
    <div class="form-row"><div class="field">Phone number</div><div class="field">Email address</div></div>
    <div class="form-row"><div class="field tall">Message</div></div>
    <span class="btn btn-navy">Send</span>
  </form>
</section>

<section class="testimonials">
  <h2 class="section-title" style="left:0;top:60px;width:1200px;text-align:center"><span style="position:relative;display:inline-block"><span class="corner"></span>Testimonials</span></h2>
  <div class="abs quote-mark">“</div>
  <div class="abs stars">
    <svg width="14" height="14" viewBox="0 0 12 12"><polygon points="6,0 7.8,4 12,4.5 8.8,7.4 9.7,12 6,9.7 2.3,12 3.2,7.4 0,4.5 4.2,4" fill="#f9b41b"/></svg>
    <svg width="14" height="14" viewBox="0 0 12 12"><polygon points="6,0 7.8,4 12,4.5 8.8,7.4 9.7,12 6,9.7 2.3,12 3.2,7.4 0,4.5 4.2,4" fill="#f9b41b"/></svg>
    <svg width="14" height="14" viewBox="0 0 12 12"><polygon points="6,0 7.8,4 12,4.5 8.8,7.4 9.7,12 6,9.7 2.3,12 3.2,7.4 0,4.5 4.2,4" fill="#f9b41b"/></svg>
    <svg width="14" height="14" viewBox="0 0 12 12"><polygon points="6,0 7.8,4 12,4.5 8.8,7.4 9.7,12 6,9.7 2.3,12 3.2,7.4 0,4.5 4.2,4" fill="#f9b41b"/></svg>
    <svg width="14" height="14" viewBox="0 0 12 12"><polygon points="6,0 7.8,4 12,4.5 8.8,7.4 9.7,12 6,9.7 2.3,12 3.2,7.4 0,4.5 4.2,4" fill="#f9b41b"/></svg>
  </div>
  <p class="abs testimonial-text">Very good service. Our property manager is very responsive and always keeps us informed. They sort out repairs quickly and make owning a rental feel easy.</p>
  <div class="abs author">Daniel R.</div>
  <svg class="abs arrow" style="left:290px" width="14" height="20" viewBox="0 0 14 20"><polygon points="12,2 2,10 12,18" fill="#1c2f45"/></svg>
  <svg class="abs arrow" style="left:896px" width="14" height="20" viewBox="0 0 14 20"><polygon points="2,2 12,10 2,18" fill="#1c2f45"/></svg>
</section>

<footer class="site-footer">
  <div class="abs foot-about">
    <div class="brand"><span class="brand-dot"></span>Brindlewood Homes</div>
    <p>Brindlewood Homes is a local agency specialising in property management and the sale of established homes. We deliver personal service, honest advice and results that last.</p>
  </div>
  <div class="abs foot-col" style="left:480px">
    <h3>Sitemap</h3>
    <ul><li>Home</li><li>About Us</li><li>Leasing</li><li>Buy</li><li>Sell</li><li>Our Team</li><li>Blog</li><li>Contact Us</li></ul>
  </div>
  <div class="abs foot-col" style="left:640px;width:220px">
    <h3>Contact Us</h3>
    <div class="line"><svg width="12" height="14" viewBox="0 0 12 14"><path d="M6 0a5 5 0 0 0-5 5c0 4 5 9 5 9s5-5 5-9a5 5 0 0 0-5-5z" fill="#f9b41b"/></svg><span>12 Harlow Street,<br>Ferncliff VIC 3095</span></div>
    <div class="line"><svg width="12" height="12" viewBox="0 0 12 12"><path d="M2 1l2.5 0 1 3-1.5 1a7 7 0 0 0 3 3l1-1.5 3 1V10a1 1 0 0 1-1 1A10 10 0 0 1 1 2a1 1 0 0 1 1-1z" fill="#f9b41b"/></svg><span>P: (03) 9555 0148<br>F: (03) 9555 0199</span></div>
    <div class="line"><svg width="12" height="10" viewBox="0 0 12 10"><rect x="0.5" y="0.5" width="11" height="9" fill="none" stroke="#f9b41b"/><path d="M0.5 0.5L6 5l5.5-4.5" fill="none" stroke="#f9b41b"/></svg><span>hello@brindlewoodhomes.com.au</span></div>
  </div>
  <div class="abs foot-col" style="left:920px">
    <h3>Follow us on</h3>
    <div class="socials"><span></span><span></span><span></span><span></span><span></span></div>
  </div>
</footer>

<div class="bottom-bar">
  <span>Contact Us &nbsp;|&nbsp; Privacy &nbsp;|&nbsp; Complaints Handling &amp; Dispute Resolution &nbsp;|&nbsp; Your Rights &amp; Duties</span>
  <span>©2024 Brindlewood Homes. All Rights Reserved.</span>
</div>

</body>
</html>
```